Flyer for an online formula one racing league

Hello.

I am looking for the perfect one page facebook/instagram style flyer for an online formula one racing league. The racing league is called 'VOLTA RACING LEAGUE'.

Information that MUST be on the new flyer is already on the old flyer I have uploaded here. In addition to including: The Volta racing league 'V' logo I have uploaded AND the text: 'Very popular, clean and competitive racing league, running for its 4th season. Why not join with a friend? Race times, Mondays, Tuesdays and Wednesdays each at 8pm UK TIME Message below for any questions. (Spacing of information is not important, however all the information in regards to the racing I have just mentioned MUST BE on the flyer, this includes info from old pic, logo and the other info I just mentioned).

It would be beneficial to have lots of dark blue on the flyer and the new flyer to be a lot different to the original flyer I uploaded, but this is not essential.

I apologise if I did not explain very well, any questions, please message me.

The best flyer should look the most attractive to someone that might be interested in joining an online formula one racing league.

I used this website before to create the perfect logo for my Sunday League team last year, and I was very impressed. I look forward to seeing your submissions.

Target Market(s)

No specific target, more something that may attract someone into joining a formula one online racing league

Industry/Entity Type

e sports/formula one

Colors
0054AA
0677BA
7BADD7
CADEEF
E8F1F8

Requirements
Must have
• Read product description please
Should not have
• Ignoring product description!

```html
<!DOCTYPE html>
<html lang="en">
<head>
<meta charset="utf-8">
<title>Volta Racing League – Season Flyer</title>
<link rel="stylesheet" href="https://fonts.googleapis.com/css2?family=Montserrat:ital,wght@0,600;0,800;0,900;1,800;1,900&family=Oswald:wght@500;600&display=swap">
<style>
  :root {
    --backdrop: #2a2a2a;
    --header-band: #e6e6f4;
    --paper: #ffffff;
    --ink-navy: #15163a;
    --pink: #ea1f7c;
    --electric-blue: #2626c9;
    --deep-blue: #10107a;
    --night-blue: #0b0b4e;
    --violet: #7a2fd6;
    --white: #ffffff;
    --track-brown: #4a3a36;
  }
  * { box-sizing: border-box; margin: 0; padding: 0; }
  html, body {
    width: 1200px; height: 1177px; overflow: hidden;
    background: var(--backdrop);
  }
  .flyer {
    position: absolute; left: 164px; top: 148px;
    width: 888px; height: 888px; overflow: hidden;
    background: var(--paper);
    font-family: "Montserrat", Arial, sans-serif;
  }
  .masthead {
    position: absolute; left: 0; top: 0; width: 100%; height: 74px;
    background: var(--header-band);
    display: flex; align-items: center; justify-content: center;
  }
  .league-title {
    font-weight: 900; font-size: 56px; letter-spacing: 2px; line-height: 1;
    white-space: nowrap;
  }
  .league-title .word-navy { color: var(--ink-navy); }
  .league-title .word-pink { color: var(--pink); }
  .league-title .word-blue { color: var(--electric-blue); }

  .brand-mark {
    position: absolute; left: 44px; top: 96px; width: 172px; height: 172px;
    border-radius: 50%; background: var(--ink-navy);
    display: flex; align-items: center; justify-content: center;
  }
  .brand-mark span {
    font-weight: 800; font-size: 104px; color: var(--white); line-height: 1;
  }

  .intro {
    position: absolute; left: 262px; top: 87px; width: 600px;
    font-family: "Oswald", "Arial Narrow", sans-serif; text-align: center;
    color: var(--ink-navy); text-transform: uppercase; white-space: nowrap;
  }
  .intro .tagline { font-weight: 600; font-size: 35px; line-height: 42px; }
  .intro .headline { font-weight: 600; font-size: 54px; line-height: 62px; }
  .intro .season {
    margin-top: 8px; padding: 3px 0 5px;
    border-top: 2px solid var(--electric-blue); border-bottom: 2px solid var(--electric-blue);
    font-weight: 600; font-size: 46px; line-height: 52px; color: var(--electric-blue);
  }
  .intro .season em { font-style: normal; color: var(--pink); }

  .panel {
    position: absolute; left: 0; top: 300px; width: 100%; height: 588px;
    background: linear-gradient(160deg, var(--deep-blue) 0%, var(--night-blue) 70%);
  }
  .track-art {
    position: absolute; left: 0; top: 560px; width: 100%; height: 328px;
    background:
      linear-gradient(100deg, transparent 0%, transparent 55%, rgba(234,31,124,.35) 100%),
      linear-gradient(180deg, rgba(11,11,78,0) 0%, var(--electric-blue) 55%, var(--pink) 85%, var(--track-brown) 100%);
  }
  .announce-band {
    position: absolute; left: 0; top: 283px; width: 778px; height: 46px;
    background: var(--pink);
    clip-path: polygon(0 0, 100% 0, 96% 100%, 0 100%);
    display: flex; align-items: center; padding-left: 32px;
  }
  .announce-band p {
    font-weight: 900; font-style: italic; font-size: 36px; color: var(--white);
    letter-spacing: 1px; white-space: nowrap;
  }
  .details {
    position: absolute; left: 31px; top: 338px; color: var(--white); white-space: nowrap;
  }
  .details h2 {
    font-weight: 900; font-style: italic; font-size: 38px; line-height: 44px; letter-spacing: 1px;
  }
  .details p { font-weight: 600; font-size: 30px; line-height: 36px; }

  .times-band {
    position: absolute; left: 0; top: 474px; width: 352px; height: 44px;
    background: linear-gradient(90deg, var(--violet), var(--electric-blue));
    clip-path: polygon(0 0, 100% 0, 95% 100%, 0 100%);
    display: flex; align-items: center; padding-left: 31px;
  }
  .times-band h3 {
    font-weight: 900; font-style: italic; font-size: 36px; color: var(--white);
    letter-spacing: 1px; white-space: nowrap;
  }
  .times-slash {
    position: absolute; left: 343px; top: 474px; width: 26px; height: 44px;
    background: var(--pink);
    clip-path: polygon(60% 0, 100% 0, 40% 100%, 0 100%);
  }
  .schedule {
    position: absolute; left: 31px; top: 531px;
    font-weight: 900; font-style: italic; font-size: 32px; line-height: 33px;
    color: var(--white); white-space: nowrap;
  }
  .contact-note {
    position: absolute; left: 31px; top: 650px;
    font-weight: 600; font-size: 22px; line-height: 28px;
    color: var(--white); white-space: nowrap;
  }
</style>
</head>
<body>
  <main class="flyer">
    <header class="masthead">
      <h1 class="league-title">
        <span class="word-navy">VOLTA</span>
        <span class="word-pink">RACING</span>
        <span class="word-blue">LEAGUE</span>
      </h1>
    </header>

    <div class="brand-mark"><span>V</span></div>

    <section class="intro">
      <p class="tagline">Very popular, clean &amp; competitive</p>
      <p class="headline">Racing league</p>
      <p class="season">Running for its <em>4th season</em></p>
    </section>

    <section class="panel"></section>
    <div class="track-art" role="img" aria-label="Illustration of a vintage single-seater race car speeding down a striped pink and blue track with light streaks"></div>

    <div class="announce-band"><p>NEW SEASON JUST STARTING!!!</p></div>

    <section class="details">
      <h2>CLEAN ONLINE RACING LEAGUE!</h2>
      <p>3 divisions currently and looking to keep growing!</p>
      <p>Why not join with a friend?</p>
    </section>

    <div class="times-band"><h3>RACE TIMES:</h3></div>
    <div class="times-slash"></div>

    <p class="schedule">Mondays, Tuesdays<br>and Wednesdays<br>8pm UK TIME</p>
    <p class="contact-note">Message below for any questions</p>
  </main>
</body>
</html>
```